Velvet Harbor Tiles Wix Website Design

We are looking for a creative Wix based website design for our new tabletop game and pop-culture collectibles company, Velvet Harbor Tiles. We are looking for something clean, simple, profession and would really like it to be as creative and original as possible. We are trying hard not to be cookie cutter and just use the standard templates. We are attaching our work-in-progress brand guide for reference. Please read though the guide as use the appropriate color pallet and fonts as per the brand guide.

Here are some similar companies in the market for reference and target the same markets as we do.

https://www.brightnook.com/
https://www.parade-fair.org/pfx
http://qz.tollmakers.com/
https://plumtarn.com/
https://www.vostrel.com/
https://www.orchardlanternplay.com/en/index/
http://www.tallpebbleyard.com/
https://www.marlowind.com/games
https://www.haybrickcraft.com/

For illustrative purposes only, please use placeholder images from similar target market websites if necessary but those will be replaced once the design has been established and before publishing.
Updates

Posting our design request during the Christmas holiday season was probably not our best idea as many of our team have not been able to participate in the feedback and evaluation processes. We would like to extend the project 5 more days in order to give the designers proper feedback on the proposals they have submitted rather than just a stars. We WILL be selecting our design choice at the end of this extension. Thanks to everyone who has already submitted. I'm confident we will have something wonderful.

Target Market(s)

Boardgamers, Gamers, Comic Books Fans, ParadeFair attendees, etc.

Number of Pages Required

3 page

Font styles to use
Sans Serif

Colors
000000
ec1f27
ffffff

Requirements
Must have
• See attached Brand Guide for color and logo references. Our company colors are Black / Red / White. Must be WIX compatible. We currently have a place holder landing page setup at www.VelvetHarborTiles.com
Nice to have
• Be creative and original.
Should not have
• no restrictions.... yet. :)

```html
<!DOCTYPE html>
<html lang="en">
<head>
<meta charset="utf-8">
<title>Velvet Harbor Tiles</title>
<link href="https://fonts.googleapis.com/css2?family=Open+Sans:wght@400;600;700&display=swap" rel="stylesheet">
<style>
:root{
  --black:#000000;
  --ink:#0d0d0f;
  --panel:#141216;
  --red:#ec1f27;
  --deep-red:#2a0505;
  --white:#ffffff;
  --muted:#b9b4bc;
  --backdrop:#ffffff;
}
*{box-sizing:border-box;margin:0;padding:0}
html,body{width:1200px;height:1200px;overflow:hidden;background:var(--backdrop);font-family:'Open Sans',sans-serif}
.page{position:absolute;left:408px;top:0;width:342px;height:1200px;background:radial-gradient(ellipse at 50% 35%,#2a1a38 0%,#141018 45%,var(--ink) 80%);overflow:hidden}
.nav{position:absolute;left:39px;top:0;width:264px;height:12px;display:flex;align-items:center;font-size:3.4px;color:var(--white)}
.brand{font-weight:600;color:var(--red);width:26px;font-size:3px;line-height:1}
.nav-links{display:flex;gap:5px}
.nav-links .active{color:var(--red)}
.nav-call{margin-left:auto;color:var(--red)}
.hero{position:absolute;left:39px;top:12px;width:264px;height:138px;background:radial-gradient(circle at 30% 70%,#3c5a2a 0%,transparent 40%),radial-gradient(circle at 72% 62%,#2b6a78 0%,transparent 40%),linear-gradient(180deg,#3a1410 0%,#6a1c12 55%,#2a0c0a 100%);text-align:center;color:var(--white)}
.hero h1{position:absolute;top:41px;width:100%;font-size:15px;font-weight:700;letter-spacing:.2px}
.hero p{position:absolute;top:63px;width:100%;font-size:3.6px;letter-spacing:1px}
.hero .btn-outline{position:absolute;left:113px;top:86px;width:38px;height:10px;border:1px solid var(--white);font-size:3.6px;line-height:8px;letter-spacing:.4px}
.card{position:absolute;width:81px;height:111px;background:linear-gradient(180deg,#1c1520,#100c12)}
.card .thumb{height:66px}
.card h3{position:absolute;left:4px;top:71px;font-size:5px;font-weight:600;color:var(--white)}
.card p{position:absolute;left:5px;top:80px;width:72px;font-size:3.1px;line-height:4.6px;color:var(--muted)}
.card .btn{position:absolute;left:0;bottom:0;width:81px;height:7px;background:var(--red);color:var(--white);font-size:3px;line-height:7px;text-align:center}
.contact{position:absolute;left:39px;top:900px;width:264px;height:142px;background:linear-gradient(180deg,#7a1210 0%,#4a0a08 55%,#1a0606 100%);color:var(--white)}
.contact h2{position:absolute;top:26px;width:100%;text-align:center;font-size:4px;font-weight:400;letter-spacing:1.2px}
.contact .rule{position:absolute;left:128px;top:37px;width:8px;height:1px;background:var(--white)}
.field{position:absolute;border-bottom:.6px solid #8a6a6a;font-size:2.8px;color:#d8c8c8;padding:1px 1px}
.field.area{border:.6px solid #8a6a6a}
.send{position:absolute;left:62px;top:108px;width:141px;height:7px;background:var(--red);font-size:3px;line-height:7px;text-align:center}
.footer{position:absolute;left:39px;top:1042px;width:264px;height:138px;background:linear-gradient(180deg,var(--deep-red),#0e0202);color:var(--red);text-align:center}
.fcol{position:absolute;top:20px;width:80px;font-size:2.8px;line-height:4.6px}
.fcol h4{font-size:3.2px;font-weight:400;letter-spacing:1.2px;margin-bottom:8px}
.subscribe{position:absolute;top:78px;width:100%;font-size:3.2px;letter-spacing:1.2px}
.sub-input{position:absolute;left:86px;top:90px;width:54px;height:8px;background:var(--white);color:#999;font-size:2.6px;line-height:8px;text-align:left;padding-left:2px}
.sub-btn{position:absolute;left:143px;top:90px;width:33px;height:8px;border:.8px solid var(--white);font-size:2.6px;line-height:6.5px;color:var(--red)}
.socials{position:absolute;top:110px;width:100%;display:flex;justify-content:center;gap:3px}
.socials span{width:2.4px;height:2.4px;border-radius:50%;background:var(--red)}
.copy{position:absolute;top:130px;width:100%;font-size:2.8px}
</style>
</head>
<body>
<div class="page">
  <header class="nav">
    <div class="brand">Velvet Harbor Tiles</div>
    <nav class="nav-links"><span>Home</span><span>About Us</span><span class="active">Shop</span><span>Blog</span><span>Newsletter</span></nav>
    <div class="nav-call">Call Us Now: (555) 014-2290</div>
  </header>

  <section class="hero" role="img" aria-label="Illustration of two cartoon dragons in a volcanic cavern">
    <h1>A WORLD LIGHT</h1>
    <p>YEARS BEYONDY OUR IMAGINATION</p>
    <div class="btn-outline">Read More</div>
  </section>

  <!-- row 1 -->
  <article class="card" style="left:39px;top:162px"><div class="thumb" role="img" aria-label="Dinosaur game title art" style="background:linear-gradient(180deg,#3b6a1c,#7aa83a 60%,#2a4a12)"></div><h3>Bcdefghijkl</h3><p>There are many variations of passages of Lorem Ipsum available, but the majority have suffered alteration in some form, by injected humour, or randomised</p><div class="btn">Read More</div></article>
  <article class="card" style="left:131px;top:162px"><div class="thumb" role="img" aria-label="Red one-eyed monster in a platform game level" style="background:linear-gradient(180deg,#6a2a5a,#a24a80 60%,#7a8a3a)"></div><h3>Bcdefghijkl</h3><p>There are many variations of passages of Lorem Ipsum available, but the majority have suffered alteration in some form, by injected humour, or randomised</p><div class="btn">Read More</div></article>
  <article class="card" style="left:222px;top:162px"><div class="thumb" role="img" aria-label="Group of colourful cartoon monsters" style="background:linear-gradient(135deg,#3fc0c0,#d03a8a 55%,#2a6aa0)"></div><h3>Bcdefghijkl</h3><p>There are many variations of passages of Lorem Ipsum available, but the majority have suffered alteration in some form, by injected humour, or randomised</p><div class="btn">Read More</div></article>
  <!-- row 2 -->
  <article class="card" style="left:39px;top:286px"><div class="thumb" role="img" aria-label="Two brown steampunk robot figures" style="background:radial-gradient(circle,#f4e4c8,#d8b888)"></div><h3>Bcdefghijkl</h3><p>There are many variations of passages of Lorem Ipsum available, but the majority have suffered alteration in some form, by injected humour, or randomised</p><div class="btn">Read More</div></article>
  <article class="card" style="left:131px;top:286px"><div class="thumb" role="img" aria-label="Pink kids imagination monster poster" style="background:radial-gradient(circle,#e090d0,#30b8c8 70%)"></div><h3>Bcdefghijkl</h3><p>There are many variations of passages of Lorem Ipsum available, but the majority have suffered alteration in some form, by injected humour, or randomised</p><div class="btn">Read More</div></article>
  <article class="card" style="left:222px;top:286px"><div class="thumb" role="img" aria-label="Green furry cartoon monster" style="background:linear-gradient(135deg,#5a3a70,#8a5aa0)"></div><h3>Bcdefghijkl</h3><p>There are many variations of passages of Lorem Ipsum available, but the majority have suffered alteration in some form, by injected humour, or randomised</p><div class="btn">Read More</div></article>
  <!-- row 3 -->
  <article class="card" style="left:39px;top:409px"><div class="thumb" role="img" aria-label="Purple one-eyed cartoon monster" style="background:linear-gradient(135deg,#6a4a90,#9a70b8)"></div><h3>Bcdefghijkl</h3><p>There are many variations of passages of Lorem Ipsum available, but the majority have suffered alteration in some form, by injected humour, or randomised</p><div class="btn">Read More</div></article>
  <article class="card" style="left:131px;top:409px"><div class="thumb" role="img" aria-label="Dark fantasy figure against a pale moon" style="background:radial-gradient(circle at 50% 40%,#f2d8dc,#c8a0a8 60%,#6a5058)"></div><h3>Bcdefghijkl</h3><p>There are many variations of passages of Lorem Ipsum available, but the majority have suffered alteration in some form, by injected humour, or randomised</p><div class="btn">Read More</div></article>
  <article class="card" style="left:222px;top:409px"><div class="thumb" role="img" aria-label="Red horned tentacle cartoon monster" style="background:linear-gradient(135deg,#6a3a70,#9a5a98)"></div><h3>Bcdefghijkl</h3><p>There are many variations of passages of Lorem Ipsum available, but the majority have suffered alteration in some form, by injected humour, or randomised</p><div class="btn">Read More</div></article>
  <!-- row 4 -->
  <article class="card" style="left:39px;top:532px"><div class="thumb" role="img" aria-label="Winged pink cartoon monster" style="background:linear-gradient(135deg,#8a5aa0,#c090c8)"></div><h3>Bcdefghijkl</h3><p>There are many variations of passages of Lorem Ipsum available, but the majority have suffered alteration in some form, by injected humour, or randomised</p><div class="btn">Read More</div></article>
  <article class="card" style="left:131px;top:532px"><div class="thumb" role="img" aria-label="Green slime cartoon monster" style="background:linear-gradient(135deg,#4a3478,#7a58a8)"></div><h3>Bcdefghijkl</h3><p>There are many variations of passages of Lorem Ipsum available, but the majority have suffered alteration in some form, by injected humour, or randomised</p><div class="btn">Read More</div></article>
  <article class="card" style="left:222px;top:532px"><div class="thumb" role="img" aria-label="Sorcerer casting a spell in a dark forest" style="background:linear-gradient(135deg,#2a2a1a,#5a4a3a 60%,#8a6a4a)"></div><h3>Bcdefghijkl</h3><p>There are many variations of passages of Lorem Ipsum available, but the majority have suffered alteration in some form, by injected humour, or randomised</p><div class="btn">Read More</div></article>
  <!-- row 5 -->
  <article class="card" style="left:39px;top:654px"><div class="thumb" role="img" aria-label="Sea creature warrior underwater" style="background:linear-gradient(180deg,#1a4a50,#3a6a6a 60%,#1a2a30)"></div><h3>Bcdefghijkl</h3><p>There are many variations of passages of Lorem Ipsum available, but the majority have suffered alteration in some form, by injected humour, or randomised</p><div class="btn">Read More</div></article>
  <article class="card" style="left:131px;top:654px"><div class="thumb" role="img" aria-label="Yellow spiky dinosaur cartoon" style="background:linear-gradient(135deg,#2a2a5a,#4a4a88)"></div><h3>Bcdefghijkl</h3><p>There are many variations of passages of Lorem Ipsum available, but the majority have suffered alteration in some form, by injected humour, or randomised</p><div class="btn">Read More</div></article>
  <article class="card" style="left:222px;top:654px"><div class="thumb" role="img" aria-label="Red three-eyed octopus cartoon monster" style="background:linear-gradient(135deg,#2a2a68,#4a4a98)"></div><h3>Bcdefghijkl</h3><p>There are many variations of passages of Lorem Ipsum available, but the majority have suffered alteration in some form, by injected humour, or randomised</p><div class="btn">Read More</div></article>
  <!-- row 6 -->
  <article class="card" style="left:39px;top:777px"><div class="thumb" role="img" aria-label="Blue horned furry cartoon monster" style="background:linear-gradient(135deg,#5a3a88,#8a60b0)"></div><h3>Bcdefghijkl</h3><p>There are many variations of passages of Lorem Ipsum available, but the majority have suffered alteration in some form, by injected humour, or randomised</p><div class="btn">Read More</div></article>
  <article class="card" style="left:131px;top:777px"><div class="thumb" role="img" aria-label="Green ogre cartoon with a club" style="background:linear-gradient(135deg,#2a3050,#3a4868)"></div><h3>Bcdefghijkl</h3><p>There are many variations of passages of Lorem Ipsum available, but the majority have suffered alteration in some form, by injected humour, or randomised</p><div class="btn">Read More</div></article>
  <article class="card" style="left:222px;top:777px"><div class="thumb" role="img" aria-label="Purple horned cartoon monster waving" style="background:linear-gradient(135deg,#2a3458,#40508a)"></div><h3>Bcdefghijkl</h3><p>There are many variations of passages of Lorem Ipsum available, but the majority have suffered alteration in some form, by injected humour, or randomised</p><div class="btn">Read More</div></article>

  <section class="contact" role="img" aria-label="Silhouette of a dragon flying toward a castle at red sunset">
    <h2>CONTACT INFORMATIONS</h2>
    <div class="rule"></div>
    <div class="field" style="left:62px;top:51px;width:69px">Name</div>
    <div class="field" style="left:134px;top:51px;width:69px">Email</div>
    <div class="field" style="left:62px;top:63px;width:141px">Phone</div>
    <div class="field area" style="left:62px;top:77px;width:141px;height:25px">Message</div>
    <div class="send">Send</div>
  </section>

  <footer class="footer">
    <div class="fcol" style="left:20px">
      <h4>OUR STORE</h4>
      Address: 12 Lantern Quay Rd<br>Harborview, VA 20000<br>Phone: (555) 014-2290<br>Email: info@velvetharbortiles.com<br>Web: www.VelvetHarborTiles.com
    </div>
    <div class="fcol" style="left:99px">
      <h4>COMPANY</h4>
      About Us<br>Shop<br>Blog<br>Newsletter
    </div>
    <div class="fcol" style="left:179px">
      <h4>MORE RESOURCES</h4>
      But I must explain to you how all this<br>idea of denouncing pleasure<br>will give you a complete...
    </div>
    <div class="subscribe">SUBSCRIBE</div>
    <div class="sub-input">Email Address</div>
    <div class="sub-btn">Subscribe Now</div>
    <div class="socials"><span></span><span></span><span></span><span></span></div>
    <div class="copy">@Velvet Harbor Tiles 2016</div>
  </footer>
</div>
</body>
</html>
```